KRT homes
KRT homes business card/letterhead
Project: KRT homes
KRT homes - Real Estate
Creative Brief
Simple
Gregory Varnell
President
742 Birch Lane Suite 3 Walpole, MA 02047
pvarnell@krtdwellings.example
krtdwellings.example
Also need business cards for Pam Teravin Broker Cell 508.555.0187 Email: pteravin@krtdwellings.example Colleen Teravin Varnell Vice President Cell 508.555.0142 Email: colleen@krtdwellings.example
Maybe large version of logo?

```html
<!DOCTYPE html>
<html lang="en">
<head>
<meta charset="utf-8">
<title>KRT homes stationery</title>
<link href="https://fonts.googleapis.com/css2?family=Open+Sans:wght@400;600;700&display=swap" rel="stylesheet">
<style>
  :root {
    --bg-light: #a3a3a3;
    --bg-dark: #767676;
    --paper: #ffffff;
    --orange: #d95a1c;
    --orange-deep: #b84612;
    --grey-swoosh: #9a9a9a;
    --navy: #1f3f8f;
    --ink: #555555;
  }
  * { margin: 0; padding: 0; box-sizing: border-box; }
  html, body { width: 1200px; height: 626px; overflow: hidden; }
  body {
    position: relative;
    font-family: "Open Sans", Arial, sans-serif;
    background: radial-gradient(ellipse at 50% 40%, var(--bg-light), var(--bg-dark));
    color: var(--ink);
  }
  .sheet {
    position: absolute;
    background: var(--paper);
    overflow: hidden;
    box-shadow: 0 2px 6px rgba(0,0,0,.35);
  }
  .sheet svg.swoosh { position: absolute; inset: 0; width: 100%; height: 100%; }
  .wordmark {
    position: absolute;
    display: flex;
    align-items: center;
    gap: 6px;
    font-weight: 700;
    color: var(--navy);
    white-space: nowrap;
  }
  .wordmark .mark { background: var(--orange); display: inline-block; }
  .small-text { position: absolute; font-size: 6px; line-height: 1.5; color: var(--ink); }

  /* letterhead */
  .letterhead { left: 233px; top: 29px; width: 427px; height: 576px; }
  .letterhead .wordmark { left: 26px; top: 34px; font-size: 24px; }
  .letterhead .wordmark .mark { width: 16px; height: 16px; }
  .letterhead .watermark {
    position: absolute; left: 40px; top: 250px; width: 260px; text-align: center;
    font-size: 52px; font-weight: 700; color: var(--navy); opacity: .12;
  }
  .letterhead .footer { left: 26px; top: 532px; }

  /* cards */
  .card-front { left: 31px; top: 199px; width: 190px; height: 101px; }
  .card-front .wordmark { left: 52px; top: 32px; font-size: 16px; }
  .card-front .wordmark .mark { width: 10px; height: 10px; }
  .card-front .web { position: absolute; left: 0; right: 0; top: 70px; text-align: center; font-size: 5px; color: var(--orange); }
  .card-back { left: 31px; top: 312px; width: 190px; height: 101px; }
  .card-back .person { position: absolute; left: 12px; top: 16px; font-size: 7px; color: var(--orange); font-weight: 600; line-height: 1.2; }
  .card-back .person span { display: block; font-size: 5px; color: var(--ink); font-weight: 400; }
  .card-back .details { left: 12px; top: 44px; font-size: 5px; }

  /* envelopes */
  .envelope-back { left: 679px; top: 77px; width: 485px; height: 240px; }
  .envelope-front { left: 679px; top: 348px; width: 485px; height: 240px; }
  .envelope-front .wordmark { left: 26px; top: 64px; font-size: 26px; }
  .envelope-front .wordmark .mark { width: 16px; height: 16px; }
  .envelope-front .return { left: 34px; top: 108px; }
</style>
</head>
<body>

<section class="sheet letterhead">
  <svg class="swoosh" viewBox="0 0 427 576" preserveAspectRatio="none">
    <path d="M427 0 L370 0 C405 120 405 420 330 576 L427 576 Z" fill="var(--grey-swoosh)"/>
    <path d="M427 0 L385 0 C420 130 420 430 352 576 L427 576 Z" fill="var(--orange)"/>
  </svg>
  <div class="wordmark"><span class="mark"></span>KRT homes</div>
  <div class="watermark">KRT homes</div>
  <p class="small-text footer">
    T 508.555.0110<br>F 508.555.0111<br>pvarnell@krtdwellings.example<br>742 Birch Lane Suite 3 Walpole, MA 02047
  </p>
</section>

<section class="sheet card-front">
  <div class="wordmark"><span class="mark"></span>KRT homes</div>
  <p class="web">krtdwellings.example</p>
</section>

<section class="sheet card-back">
  <svg class="swoosh" viewBox="0 0 190 101" preserveAspectRatio="none">
    <path d="M190 0 L150 0 C170 30 165 70 140 101 L190 101 Z" fill="var(--grey-swoosh)"/>
    <path d="M190 0 L158 0 C178 30 174 72 150 101 L190 101 Z" fill="var(--orange)"/>
  </svg>
  <p class="person">Gregory Varnell<span>President</span></p>
  <p class="small-text details">
    T 508.555.0110<br>pvarnell@krtdwellings.example<br>krtdwellings.example<br>742 Birch Lane Suite 3 Walpole, MA 02047
  </p>
</section>

<section class="sheet envelope-back">
  <svg class="swoosh" viewBox="0 0 485 240" preserveAspectRatio="none">
    <defs>
      <linearGradient id="flapGradient" x1="0" y1="0" x2="1" y2="0">
        <stop offset="0" stop-color="var(--orange-deep)"/>
        <stop offset="0.5" stop-color="var(--orange)"/>
        <stop offset="1" stop-color="var(--orange-deep)"/>
      </linearGradient>
    </defs>
    <path d="M0 0 H485 V95 L330 120 H155 L0 95 Z" fill="url(#flapGradient)"/>
  </svg>
</section>

<section class="sheet envelope-front">
  <svg class="swoosh" viewBox="0 0 485 240" preserveAspectRatio="none">
    <path d="M485 60 C470 140 430 200 360 240 L485 240 Z" fill="var(--grey-swoosh)"/>
    <path d="M485 80 C475 150 445 205 385 240 L485 240 Z" fill="var(--orange)"/>
  </svg>
  <div class="wordmark"><span class="mark"></span>KRT homes</div>
  <p class="small-text return">
    T 508.555.0110<br>pvarnell@krtdwellings.example<br>742 Birch Lane Suite 3 Walpole, MA 02047
  </p>
</section>

</body>
</html>
```